Book cover design for modern bagpipe music book

This music book will be A4 in size and requires a design for the front and back cover. The focus is on creating a modern and eye catching design, breaking away from the stereotypes of what people think of when they think of bagpipes. Think the OPPOSITE of a bagpiper in a full kilt standing on top of a mountain playing Copper Lanterns Rising!

Book title: Rise Hum March Rest

Other front cover text : Music for the bagpipes by Dermot Fairley

Front cover file ideas uploaded

2 pictures of bagpipes attached.

- The real set of bagpipes give an idea of the correct finer details

- The toy bagpipes perhaps have a better shape with the left 'stick' down

Back cover - No real brief. Keen for it not to be a full block single colour though.

Design requires 3mm bleed for print

Open to ideas and suggestions! Thank you!

```html
<!DOCTYPE html>
<html lang="en">
<head>
<meta charset="utf-8">
<title>Rise Hum March Rest — Book Cover</title>
<link rel="stylesheet" href="https://fonts.googleapis.com/css2?family=Montserrat:wght@400;600;700&family=Oswald:wght@300&family=Roboto:wght@700&display=swap">
<style>
  :root {
    --paper: #ffffff;
    --rust: #9a4512;
    --rust-deep: #6e2a08;
    --rust-dark: #4a1606;
    --tartan-red: #b8301a;
    --tartan-dark: #7a1c10;
    --ink: #ffffff;
    --shadow: #1d0c04;
    --icon-ink: #8a3a10;
    --label: #111111;
  }
  * { margin: 0; padding: 0; box-sizing: border-box; }
  html, body { width: 1200px; height: 924px; overflow: hidden; background: var(--paper); }
  .spread { position: relative; width: 1200px; height: 924px; }

  .cover {
    position: absolute; top: 20px; width: 586px; height: 830px; overflow: hidden;
    background:
      radial-gradient(ellipse at 50% 40%, rgba(160,80,25,0.55), transparent 70%),
      linear-gradient(180deg, var(--rust) 0%, #8c3c0f 60%, var(--rust-deep) 88%, var(--rust-dark) 100%);
  }
  .cover--back { left: 9px; }
  .cover--front { left: 602px; }

  .tartan-band {
    position: absolute; top: 0; height: 100%;
    background:
      linear-gradient(180deg, rgba(122,28,16,0.55) 0%, rgba(184,48,26,0.55) 30%, rgba(160,40,22,0.6) 60%, rgba(110,30,14,0.55) 100%),
      linear-gradient(90deg, var(--tartan-dark), var(--tartan-red) 40%, var(--tartan-red) 70%, var(--tartan-dark));
    opacity: 0.85;
  }
  .cover--back .tartan-band { left: 359px; width: 227px; }
  .cover--front .tartan-band { left: 0; width: 222px; }

  .title-list { position: absolute; left: 76px; top: 0; list-style: none; }
  .title-row { position: absolute; left: 0; display: flex; align-items: center; }
  .title-row:nth-child(1) { top: 102px; }
  .title-row:nth-child(2) { top: 241px; }
  .title-row:nth-child(3) { top: 382px; }
  .title-row:nth-child(4) { top: 525px; }

  .icon-tile {
    width: 111px; height: 107px; border: 2px solid var(--ink); border-radius: 12px;
    padding: 5px; flex: none;
  }
  .icon-tile__inner {
    width: 100%; height: 100%; background: var(--ink); border-radius: 8px;
    display: flex; align-items: center; justify-content: center;
  }
  .icon-tile svg { width: 76px; height: 76px; }
  .icon-placeholder { width: 76px; height: 76px; background: var(--icon-ink); border-radius: 4px; opacity: 0.85; }

  .title-word {
    margin-left: 27px;
    font-family: "Montserrat", sans-serif; font-weight: 600; font-size: 80px;
    letter-spacing: 2px; color: var(--ink); line-height: 1;
    text-shadow: 4px 4px 0 var(--shadow);
  }

  .subtitle {
    position: absolute; left: 0; width: 100%; text-align: center; top: 737px;
    padding-left: 28px;
    font-family: "Oswald", sans-serif; font-weight: 300; font-size: 27px;
    color: var(--ink); letter-spacing: 0.5px; text-transform: uppercase;
    transform: scaleX(0.82);
  }
  .author {
    position: absolute; left: 159px; top: 780px;
    font-family: "Montserrat", sans-serif; font-weight: 400; font-size: 27px;
    color: var(--ink); letter-spacing: 2px; text-transform: uppercase;
  }

  .side-label {
    position: absolute; top: 876px; width: 586px; text-align: center;
    font-family: "Roboto", sans-serif; font-weight: 700; font-size: 28px; color: var(--label);
  }
  .side-label--back { left: 9px; }
  .side-label--front { left: 602px; }
</style>
</head>
<body>
<main class="spread">
  <section class="cover cover--back" aria-label="Back cover">
    <div class="tartan-band" role="img" aria-label="Red tartan fabric band running down the spine"></div>
  </section>

  <section class="cover cover--front" aria-label="Front cover">
    <div class="tartan-band" role="img" aria-label="Red tartan fabric band running down the spine"></div>

    <ol class="title-list">
      <li class="title-row">
        <div class="icon-tile"><div class="icon-tile__inner">
          <svg viewBox="0 0 76 76" aria-hidden="true">
            <rect x="2" y="2" width="72" height="72" rx="4" fill="var(--icon-ink)"/>
            <line x1="14" y1="12" x2="60" y2="62" stroke="#fff" stroke-width="8" stroke-linecap="round"/>
            <line x1="62" y1="18" x2="16" y2="62" stroke="#fff" stroke-width="6" stroke-linecap="round"/>
            <line x1="56" y1="8" x2="56" y2="22" stroke="#fff" stroke-width="3"/>
            <line x1="62" y1="10" x2="62" y2="24" stroke="#fff" stroke-width="3"/>
            <line x1="68" y1="14" x2="68" y2="26" stroke="#fff" stroke-width="3"/>
          </svg>
        </div></div>
        <span class="title-word">RISE</span>
      </li>
      <li class="title-row">
        <div class="icon-tile"><div class="icon-tile__inner">
          <svg viewBox="0 0 76 76" aria-hidden="true">
            <rect x="2" y="2" width="72" height="72" rx="4" fill="var(--icon-ink)"/>
            <text x="34" y="24" fill="#fff" font-family="Montserrat, sans-serif" font-size="13" font-weight="700">zZZ</text>
            <rect x="10" y="28" width="5" height="32" fill="#fff"/>
            <rect x="61" y="40" width="5" height="20" fill="#fff"/>
            <rect x="15" y="44" width="46" height="8" fill="#fff"/>
            <rect x="20" y="36" width="40" height="8" rx="3" fill="#fff"/>
          </svg>
        </div></div>
        <span class="title-word">HUM</span>
      </li>
      <li class="title-row">
        <div class="icon-tile"><div class="icon-tile__inner">
          <div class="icon-placeholder" role="img" aria-label="Bagpipes pictogram"></div>
        </div></div>
        <span class="title-word">MARCH</span>
      </li>
      <li class="title-row">
        <div class="icon-tile"><div class="icon-tile__inner">
          <svg viewBox="0 0 76 76" aria-hidden="true">
            <rect x="2" y="2" width="72" height="72" rx="4" fill="var(--icon-ink)"/>
            <path d="M16 44 V24 H48" fill="none" stroke="#fff" stroke-width="7"/>
            <polygon points="46,12 62,24 46,36" fill="#fff"/>
            <path d="M60 32 V52 H28" fill="none" stroke="#fff" stroke-width="7"/>
            <polygon points="30,40 14,52 30,64" fill="#fff"/>
          </svg>
        </div></div>
        <span class="title-word">REST</span>
      </li>
    </ol>

    <p class="subtitle">Music for Bagpipes</p>
    <p class="author">By: Dermot Fairley</p>
  </section>

  <p class="side-label side-label--back">BACK</p>
  <p class="side-label side-label--front">FRONT</p>
</main>
</body>
</html>
```